website design for online company - registration of companies AUSTRALIA

website name: velmora482.com.au
purpose of the website: register NEW australian companies

once a client submits their order, our website will submit information to a government agency and in under 20 minutes, the client will receive their new company together with legal documentation:

key features:
- simplicity
- ease of use
- clarity
- fast
- competitive
- trust

our competitors:
www.quickdratel.com.au
www.zentrafirms.com.au

the website needs to be dynamic, clear and portray simplicity as the name suggests.

"register your company online with OREV in 3 simple steps"
1 fill in a short form
2 submit payment
3 receive your company

headings - similar to our competitors but needs to be different.

Design only no coding

if you have any questions, feel free to ask

people in business

Government

Serif

• simple
creative
elegant
• top graphics

```html
<!DOCTYPE html>
<html lang="en">
<head>
<meta charset="utf-8">
<title>Velmora482 – Online Company Registration</title>
<link rel="stylesheet" href="https://fonts.googleapis.com/css2?family=PT+Sans:wght@400;700&family=Ubuntu:wght@400;500&family=Courgette&display=swap">
<style>
  :root {
    --blue: #1a9ad6;
    --blue-dark: #1672b0;
    --red: #e04a2a;
    --charcoal: #555555;
    --text: #666666;
    --pink: #f0a9a0;
    --footer-bg: #ececec;
    --white: #ffffff;
  }
  * { box-sizing: border-box; margin: 0; padding: 0; }
  html, body { width: 934px; height: 1200px; overflow: hidden; background: var(--white); }
  body { position: relative; font-family: "PT Sans", Tahoma, sans-serif; color: var(--text); }
  .abs { position: absolute; }

  /* header */
  .site-header { position: absolute; left: 0; top: 0; width: 934px; height: 48px; background: var(--white); border-top: 3px solid var(--blue); }
  .brand { position: absolute; left: 125px; top: 8px; }
  .brand-name { font-family: "Ubuntu", sans-serif; font-weight: 500; font-size: 23px; color: var(--blue-dark); letter-spacing: .5px; line-height: 1; }
  .brand-tag { font-size: 12px; color: var(--text); margin-top: 2px; }
  .main-nav { position: absolute; right: 125px; top: 17px; display: flex; gap: 13px; font-size: 13px; }
  .main-nav a { color: #444; text-decoration: none; }
  .main-nav a.is-active { color: var(--blue); }

  /* hero */
  .hero { position: absolute; left: 0; top: 48px; width: 934px; height: 342px; background: linear-gradient(160deg, #c9ccd3 0%, #e4e6ea 40%, #d3d7dd 70%, #aeb6c0 100%); border-bottom: 3px solid var(--pink); }
  .hero-title { position: absolute; left: 125px; top: 78px; font-family: "Ubuntu", sans-serif; font-size: 31px; color: var(--blue-dark); letter-spacing: 1px; }
  .hero-title span { color: var(--red); }
  .hero-sub { position: absolute; left: 125px; top: 115px; font-family: "Ubuntu", sans-serif; font-size: 22px; color: var(--blue-dark); letter-spacing: .6px; }
  .hero-text { position: absolute; left: 125px; top: 153px; width: 400px; font-size: 17px; line-height: 25px; color: #555; letter-spacing: .4px; }
  .hero-clock { position: absolute; left: 542px; top: 106px; }

  .btn { position: absolute; display: flex; align-items: center; justify-content: center; background: var(--blue); color: var(--white); border-radius: 3px; border: 1px solid #0f7fb5; font-size: 15px; text-decoration: none; }

  /* steps */
  .steps { position: absolute; left: 0; top: 393px; width: 934px; height: 259px; background: var(--blue); }
  .steps-title { position: absolute; left: 0; width: 934px; top: 20px; text-align: center; font-family: "Ubuntu", sans-serif; font-size: 25px; color: var(--white); letter-spacing: .5px; text-shadow: 0 1px 2px rgba(0,0,0,.25); }
  .step { position: absolute; width: 164px; height: 164px; border-radius: 50%; border: 4px solid var(--white); color: var(--white); text-align: center; font-family: "Courgette", cursive; font-size: 20px; line-height: 29px; padding-top: 86px; box-shadow: 0 2px 4px rgba(0,0,0,.25); }
  .step svg { position: absolute; left: 56px; top: 22px; }
  .step--red { background: var(--red); }
  .step--grey { background: var(--charcoal); }

  /* why */
  .why-title { position: absolute; left: 126px; top: 677px; font-family: "Ubuntu", sans-serif; font-size: 21px; color: var(--blue-dark); }
  .why-title span { color: var(--red); }
  .why-rule { position: absolute; left: 270px; top: 696px; width: 539px; height: 2px; background: var(--blue); }
  .why-copy { position: absolute; left: 126px; top: 731px; width: 332px; font-family: Tahoma, "PT Sans", sans-serif; font-size: 12.4px; line-height: 14px; color: #777; }
  .why-copy p + p { margin-top: 14px; }
  .why-photo { position: absolute; left: 475px; top: 733px; width: 333px; height: 191px; border-radius: 4px; background: linear-gradient(170deg, #c3cad3 0%, #7d8896 45%, #2f4c74 80%, #4a5563 100%); box-shadow: 0 2px 3px rgba(0,0,0,.2); }

  /* name check */
  .name-check { position: absolute; left: 0; top: 996px; width: 934px; height: 67px; background: var(--charcoal); border-bottom: 3px solid var(--pink); }
  .name-check-label { position: absolute; left: 144px; top: 24px; font-size: 15px; color: var(--white); letter-spacing: .4px; }
  .name-check-input { position: absolute; left: 457px; top: 19px; width: 223px; height: 29px; background: var(--white); font-size: 13px; color: #c8c8c8; padding: 6px 12px; }
  .name-check-btn { position: absolute; left: 680px; top: 19px; width: 108px; height: 29px; background: var(--red); color: var(--white); font-size: 15px; display: flex; align-items: center; justify-content: center; }

  /* footer */
  .site-footer { position: absolute; left: 0; top: 1066px; width: 934px; height: 104px; background: var(--footer-bg); }
  .footer-heading { position: absolute; font-size: 11px; color: #555; }
  .footer-list { position: absolute; list-style: none; font-size: 9px; line-height: 13.5px; color: #666; }
  .social-dot { position: absolute; top: 35px; width: 17px; height: 17px; border-radius: 50%; background: #9a9a9a; }
  .card-chip { position: absolute; top: 36px; width: 28px; height: 17px; border-radius: 2px; }
  .copyright { position: absolute; left: 0; top: 1170px; width: 934px; height: 30px; background: var(--blue); color: var(--white); font-size: 8px; text-align: center; padding-top: 9px; }
</style>
</head>
<body>

<header class="site-header">
  <div class="brand">
    <div class="brand-name">VELMORA482</div>
    <div class="brand-tag">Company Legal Documents</div>
  </div>
  <nav class="main-nav">
    <a class="is-active" href="#">Home</a>
    <a href="#">Register a Company</a>
    <a href="#">How it works</a>
    <a href="#">FAQ</a>
    <a href="#">Legal Forms</a>
    <a href="#">Contact us</a>
  </nav>
</header>

<section class="hero" role="img" aria-label="Photo of office towers seen from below against a cloudy sky">
  <h1 class="hero-title">In <span>20 Minutes</span></h1>
  <h2 class="hero-sub">Online Company Registration</h2>
  <p class="hero-text">A simple and efficient registration process and I would recommend it to anyone</p>
  <a class="btn" href="#" style="left:0;top:227px;position:absolute;margin-left:126px;width:132px;height:29px;">Register Now</a>
  <svg class="hero-clock" width="120" height="120" viewBox="0 0 120 120">
    <circle cx="60" cy="60" r="57" fill="none" stroke="#1a9ad6" stroke-width="2.5"/>
    <line x1="60" y1="60" x2="50" y2="12" stroke="#1a9ad6" stroke-width="2"/>
    <line x1="60" y1="60" x2="100" y2="77" stroke="#1a9ad6" stroke-width="2"/>
  </svg>
</section>

<section class="steps">
  <h2 class="steps-title">Register your company online with OREV in 3 simple steps</h2>

  <svg class="abs" style="left:270px;top:70px" width="400" height="180" viewBox="0 0 400 180">
    <defs>
      <marker id="arrowhead" markerWidth="6" markerHeight="6" refX="3" refY="3" orient="auto">
        <path d="M0,0 L6,3 L0,6 Z" fill="#3a3a3a"/>
      </marker>
    </defs>
    <path d="M18,110 Q50,160 110,130" fill="none" stroke="#3a3a3a" stroke-width="7" marker-end="url(#arrowhead)"/>
    <path d="M265,45 Q320,-5 370,52" fill="none" stroke="#3a3a3a" stroke-width="7" marker-end="url(#arrowhead)"/>
  </svg>

  <div class="step step--red" style="left:127px;top:75px;">
    <svg width="44" height="44" viewBox="0 0 44 44"><rect x="4" y="12" width="34" height="26" fill="none" stroke="#fff" stroke-width="3"/><line x1="10" y1="22" x2="26" y2="22" stroke="#fff" stroke-width="2.5"/><line x1="10" y1="29" x2="30" y2="29" stroke="#fff" stroke-width="2.5"/><line x1="22" y1="22" x2="38" y2="4" stroke="#fff" stroke-width="4"/></svg>
    Fill a<br>Short form
  </div>
  <div class="step step--grey" style="left:385px;top:75px;">
    <svg width="44" height="44" viewBox="0 0 44 44"><rect x="12" y="6" width="28" height="20" rx="2" fill="none" stroke="#fff" stroke-width="3"/><line x1="12" y1="13" x2="40" y2="13" stroke="#fff" stroke-width="3"/><path d="M4,24 L14,20 L24,26 L20,32 L10,38 Z" fill="#fff"/></svg>
    Submit<br>Payment
  </div>
  <div class="step step--red" style="left:643px;top:75px;">
    <svg width="44" height="44" viewBox="0 0 44 44"><rect x="6" y="6" width="26" height="18" rx="2" fill="#fff" transform="rotate(-12 19 15)"/><rect x="12" y="16" width="28" height="20" rx="2" fill="#fff" stroke="#e04a2a" stroke-width="2"/><line x1="12" y1="23" x2="40" y2="23" stroke="#e04a2a" stroke-width="3"/></svg>
    Receive your<br>Company
  </div>
</section>

<h2 class="why-title">Why <span>choose us</span></h2>
<div class="why-rule"></div>
<div class="why-copy">
  <p>Lorem ipsum dolor sit amet, fames purus, quam mattis morbi id. Orci nam dolor ligula aliquam, lacus turpis. Donec magna sodales tincidunt condimentum nunc, mi id convallis lorem, eros massa varius a. In integer sit, eu vitae hac. Nec enim vestibulum, suspendisse suscipit penatibus est lectus nulla nec, dictum non wisi, convallis duis nullam consectetuer pretium.</p>
  <p>Lorem ipsum dolor sit amet, fames purus, quam mattis morbi id. Orci nam dolor ligula aliquam, lacus turpis. Donec magna sodales tincidunt condimentum nunc, mi id convallis lorem, eros massa varius a. In integer sit, eu vitae hac. Nec enim vestibulum.</p>
</div>
<div class="why-photo" role="img" aria-label="Photo of a curved glass office tower among high-rise buildings"></div>
<a class="btn" href="#" style="left:126px;top:924px;width:92px;height:29px;">View More</a>

<section class="name-check">
  <div class="name-check-label">CHECK YOUR COMPANY NAME AVAILABILITY</div>
  <div class="name-check-input">Company Name</div>
  <div class="name-check-btn">Check Now</div>
</section>

<footer class="site-footer">
  <div class="footer-heading" style="left:126px;top:17px;">Our Services And FAQ</div>
  <ul class="footer-list" style="left:126px;top:32px;">
    <li>Document Printing</li><li>Register a company</li><li>Domain Registration</li><li>ABN Registration</li>
  </ul>
  <ul class="footer-list" style="left:233px;top:32px;">
    <li>Velmora482</li><li>ABN Registration</li><li>FAQ's</li>
  </ul>

  <div class="footer-heading" style="left:349px;top:15px;">Links</div>
  <ul class="footer-list" style="left:349px;top:32px;">
    <li>Register a Company</li><li>How it works</li><li>Legal Forms</li><li>Contact Us</li>
  </ul>

  <div class="footer-heading" style="left:475px;top:15px;">Social networks</div>
  <span class="social-dot" style="left:475px;"></span>
  <span class="social-dot" style="left:502px;"></span>
  <span class="social-dot" style="left:529px;"></span>
  <span class="social-dot" style="left:556px;"></span>

  <div class="footer-heading" style="left:649px;top:15px;">Payment</div>
  <span class="card-chip" style="left:649px;background:#c9452f;"></span>
  <span class="card-chip" style="left:683px;background:#3b7cc0;"></span>
  <span class="card-chip" style="left:717px;background:#2f4c9a;"></span>
  <span class="card-chip" style="left:751px;background:#1f3b8a;"></span>
  <span class="card-chip" style="left:785px;background:#c9452f;"></span>
</footer>

<div class="copyright">Copyright © 2012 Velmora482. All rights reserved.</div>

</body>
</html>
```